Redesign PixelHarbor's Designer Account Home Page

Are a web designer? New to PixelHarbor? This contest is for you!

We want you to redesign PixelHarbor's designer account home page. We're looking for bold and innovative ideas to make this page a useful and fun experience for you and your fellow designers.

Only new registrants this month are eligible to enter this contest and win prizes.

Your task:
* We want you to put your web design skills to the test and re-design the My Account home page ("Overview") on PixelHarbor to make it more functional and engaging for designers on PixelHarbor.
* The page you are redesigning is here: http://www.pixelharbor-example.com/my-profile.
* Your design should allow for the same functionality as the existing page, though you don't need to replicate the same elements (buttons) or the same menu structure.
* Your design must fit with the branding of the site.
* You must provide a brief outline of what changes you made and why when you upload your design
* 1 submission per designer - make it your best work!
* Pls see "Must haves" for requirements.

Deadline:
* Submit before 12:00am 1st September UTC. Pls convert this deadline to your local timezone and take note of the local time and date

Prizes: $1,000 to win
* First prize for the best design is $700
* Second prize is $200
* Third prize is $100

If you started from scratch, how would you design the MyAccount page on PixelHarbor?

Good luck & have fun!

Mel / The PixelHarbor Team

Target Market(s)

PixelHarbor designers

Number of Pages Required

1 page

Requirements
Must have
• Dimensions: 1200 x 1000 px
• Minimum 150-300 dpi
• Your design must adhere to our quality standards to be eligible to receive a prize
• Submissions must be created in Adobe Creative Suite (Illustrator or Photoshop)
• Your design must fit with the branding of the PixelHarbor site.
• Only new registrants this month are eligible to enter and win prizes.

```html
<!DOCTYPE html>
<html lang="en">
<head>
<meta charset="utf-8">
<title>PixelHarbor – My Profile Overview</title>
<link href="https://fonts.googleapis.com/css2?family=Open+Sans:wght@400;600;700&display=swap" rel="stylesheet">
<style>
:root{
  --page:#eef0f2;
  --white:#ffffff;
  --ink:#333a40;
  --muted:#8a9299;
  --line:#dde1e4;
  --blue:#1a8bc8;
  --blue-dark:#136d9e;
  --green:#7cb82f;
  --red:#e0413a;
  --track:#d9dde0;
  --footer:#2f3236;
  --footer-deep:#25282b;
  --footer-text:#a6abb0;
}
*{box-sizing:border-box;margin:0;padding:0}
html,body{width:1200px;height:2212px;overflow:hidden}
body{background:var(--page);font-family:"Open Sans",Arial,sans-serif;color:var(--ink);font-size:12px;position:relative}
.abs{position:absolute}

/* header */
.site-header{left:0;top:0;width:1200px;height:36px;background:var(--white);border-bottom:1px solid var(--line)}
.brand{left:60px;top:7px;display:flex;align-items:center;gap:6px;font-weight:700;font-size:17px;color:var(--blue-dark)}
.brand-dot{width:18px;height:18px;border-radius:50%;background:var(--blue)}
.main-nav{left:228px;top:11px;display:flex;gap:14px;font-size:11px;font-weight:600;color:var(--ink)}
.phone{left:710px;top:11px;font-size:10px;color:var(--muted)}
.flag-chip{left:790px;top:12px;width:16px;height:11px;background:#2c4f9e}
.profile-menu{left:896px;top:8px;width:120px;height:20px;border:1px solid var(--line);font-size:10px;padding:3px 8px;color:var(--ink)}
.browse-btn{left:1030px;top:7px;width:94px;height:22px;background:var(--green);color:var(--white);font-size:10px;font-weight:700;text-align:center;line-height:22px;border-radius:2px}

.crumbs{left:0;top:36px;width:1200px;height:22px;background:#e4e7ea;border-bottom:1px solid var(--line);font-size:10px;color:var(--muted);padding:5px 60px;display:flex;gap:18px}
.crumbs b{color:var(--ink);font-weight:600}

.page-title{left:0;top:78px;width:1200px;text-align:center;font-size:26px;font-weight:700;color:var(--ink)}
.title-rule{left:60px;top:122px;width:1064px;height:1px;background:var(--line)}

/* sidebar */
.sidebar{left:60px;top:222px;width:140px;height:370px;background:var(--white);border:1px solid var(--line)}
.side-head{height:44px;background:var(--green);color:var(--white);font-size:17px;font-weight:700;padding:10px 12px}
.side-menu{list-style:none}
.side-menu li{height:38px;border-bottom:1px solid var(--line);font-size:10px;color:var(--muted);padding:12px 12px 0 34px;position:relative}
.side-menu li::before{content:"";position:absolute;left:14px;top:13px;width:10px;height:10px;border:1px solid #b6bcc1;border-radius:2px}
.side-menu li.active{background:var(--blue);color:var(--white)}
.side-menu li.active::before{border-color:var(--white)}

/* cards */
.card{background:var(--white);border:1px solid var(--line)}
.profile-card{left:212px;top:222px;width:350px;height:370px}
.profile-band{height:112px;background:var(--blue);position:relative}
.avatar{position:absolute;left:139px;top:30px;width:72px;height:72px;border-radius:50%;background:#cfe6f4;border:4px solid var(--white)}
.stats{display:grid;grid-template-columns:1fr 1fr;padding:18px 24px;gap:22px 16px}
.stat{display:flex;gap:10px;border-bottom:1px solid var(--line);padding-bottom:16px}
.stat-icon{width:30px;height:30px;border-radius:50%;background:var(--blue);flex:none}
.stat-label{font-size:11px;font-weight:700;color:var(--blue-dark)}
.stat-value{font-size:15px;font-weight:700}
.stat-note{font-size:9px;color:var(--muted)}

.progress-card{left:574px;top:222px;width:550px;height:370px}
.progress-card h2{font-size:26px;font-weight:700;padding:22px 24px 0;line-height:1.1}
.progress-card h3{font-size:17px;font-weight:600;color:var(--ink);padding:4px 24px 0}
.donut{left:158px;top:112px}
.pct-tag{left:326px;top:108px;background:#4a5157;color:var(--white);font-size:10px;font-weight:700;padding:3px 6px;border-radius:2px}

.section{left:212px;width:912px}
.section h2{font-size:20px;font-weight:700;padding:14px 18px 6px;border-bottom:1px solid var(--line)}
.intro{font-size:10px;color:var(--muted);padding:6px 18px}
.todo{top:650px;height:372px}
.todo-list{list-style:none;padding:6px 18px}
.todo-list li{height:38px;border-bottom:1px solid var(--line);display:flex;align-items:center;font-size:11px;color:var(--ink);position:relative;padding-left:20px}
.todo-list li::before{content:"";position:absolute;left:2px;width:8px;height:8px;border-radius:50%;background:#c3c8cc}
.todo-list li.done{font-weight:700}
.todo-list .check{margin-left:auto}
.todo-list .complete{margin-left:auto;color:var(--red);font-weight:700;font-size:10px}

.jobs{top:1040px;height:342px}
.job-grid{display:grid;grid-template-columns:repeat(3,1fr);gap:14px;padding:6px 18px}
.job{border:1px solid var(--line);height:104px;display:flex;gap:10px;padding:12px}
.job-badge{width:56px;height:56px;border-radius:50%;border:5px solid var(--blue);background:#e7f2f9;flex:none}
.job h4{font-size:12px;font-weight:600;color:var(--blue-dark);margin-top:6px;white-space:nowrap}
.job-meta{display:flex;gap:4px;margin-top:12px;font-size:9px;color:var(--muted);white-space:nowrap}
.job-meta span{border:1px solid var(--line);padding:3px 4px}
.pager{display:flex;justify-content:space-between;padding:10px 18px;font-size:10px;color:var(--muted)}

.achievements{top:1404px;height:206px}
.ach-grid{display:grid;grid-template-columns:1fr 1fr;gap:10px 16px;padding:8px 18px 16px}
.ach{border:1px solid var(--line);height:46px;display:flex;align-items:center;gap:10px;padding:0 10px}
.ach-icon{width:26px;height:26px;border-radius:50%;background:var(--blue);flex:none}
.ach b{font-size:11px;color:var(--blue-dark);display:block}
.ach small{font-size:9px;color:var(--muted)}

/* footer */
.site-footer{left:0;top:1700px;width:1200px;height:482px;background:var(--footer)}
.foot-col{top:1740px;font-size:11px;color:var(--footer-text)}
.foot-col h5{font-size:15px;font-weight:700;color:var(--white);margin-bottom:20px}
.foot-col li{list-style:none;border-bottom:1px solid #3d4146;padding:9px 0;width:120px}
.tags{display:flex;flex-wrap:wrap;gap:6px;width:240px}
.tags span{background:#44494e;color:#d0d3d6;padding:4px 7px;font-size:10px}
.news input{width:250px;height:28px;border:none;background:#45494e}
.socials{display:flex;gap:8px;margin-top:24px}
.socials span{width:32px;height:32px;border-radius:3px}
.flags{display:flex;gap:6px;margin-top:30px}
.flags span{width:24px;height:16px;background:#6b7177}
.foot-brand{margin-top:30px;font-size:18px;font-weight:700;color:var(--white);display:flex;gap:6px;align-items:center}
.copyright{left:0;top:2182px;width:1200px;height:30px;background:var(--footer-deep);color:#7c8288;font-size:9px;text-align:center;line-height:30px}
</style>
</head>
<body>

<header class="site-header abs">
  <div class="brand abs"><span class="brand-dot"></span>PixelHarbor</div>
  <nav class="main-nav abs"><span>Categories</span><span>Designers</span><span>Browse Jobs</span><span>How it works</span></nav>
  <div class="phone abs">1300 555 012</div>
  <div class="flag-chip abs" role="img" aria-label="Region flag"></div>
  <div class="profile-menu abs">My Profile ▾</div>
  <div class="browse-btn abs">Browse Jobs ›</div>
</header>
<div class="crumbs abs"><b>⌂ Home</b><span>My Profile</span></div>

<h1 class="page-title abs">Overview</h1>
<div class="title-rule abs"></div>

<aside class="sidebar abs">
  <div class="side-head">Browse Jobs</div>
  <ul class="side-menu">
    <li class="active">Overview</li>
    <li>Notifications</li>
    <li>Profile</li>
    <li>Submissions</li>
    <li>Messages</li>
    <li>Watchlist</li>
    <li>Widgets</li>
    <li>My Profile</li>
  </ul>
</aside>

<section class="card profile-card abs">
  <div class="profile-band"><div class="avatar" role="img" aria-label="Designer profile avatar"></div></div>
  <div class="stats">
    <div class="stat"><span class="stat-icon"></span><div><div class="stat-label">Rank</div><div class="stat-value"># 456577</div><div class="stat-note">of 512,118 designers</div></div></div>
    <div class="stat"><span class="stat-icon"></span><div><div class="stat-label">Position</div>
      <svg width="62" height="12" viewBox="0 0 62 12"><g fill="#f3b51c"><polygon points="6,0 7.8,4 12,4.4 8.8,7.2 9.7,11.5 6,9.3 2.3,11.5 3.2,7.2 0,4.4 4.2,4"/><polygon transform="translate(12.5 0)" points="6,0 7.8,4 12,4.4 8.8,7.2 9.7,11.5 6,9.3 2.3,11.5 3.2,7.2 0,4.4 4.2,4"/></g><g fill="#c9cdd1"><polygon transform="translate(25 0)" points="6,0 7.8,4 12,4.4 8.8,7.2 9.7,11.5 6,9.3 2.3,11.5 3.2,7.2 0,4.4 4.2,4"/><polygon transform="translate(37.5 0)" points="6,0 7.8,4 12,4.4 8.8,7.2 9.7,11.5 6,9.3 2.3,11.5 3.2,7.2 0,4.4 4.2,4"/><polygon transform="translate(50 0)" points="6,0 7.8,4 12,4.4 8.8,7.2 9.7,11.5 6,9.3 2.3,11.5 3.2,7.2 0,4.4 4.2,4"/></g></svg>
      <div class="stat-value">40%</div></div></div>
    <div class="stat"><span class="stat-icon"></span><div><div class="stat-label">Submissions</div><div class="stat-value">112</div><div class="stat-note">site average 71</div></div></div>
    <div class="stat"><span class="stat-icon"></span><div><div class="stat-label">Earnings</div><div class="stat-value">$1200.00</div><div class="stat-note">site average $380</div></div></div>
  </div>
</section>

<section class="card progress-card abs">
  <h2>Getting Started</h2>
  <h3>Complete Your Profile</h3>
  <svg class="donut abs" width="220" height="220" viewBox="0 0 220 220">
    <circle cx="110" cy="110" r="90" fill="none" stroke="var(--track)" stroke-width="22"/>
    <circle cx="110" cy="110" r="90" fill="none" stroke="var(--blue)" stroke-width="22" stroke-dasharray="407.2 565.5" transform="rotate(-90 110 110)"/>
    <text x="110" y="118" text-anchor="middle" font-family="Open Sans, sans-serif" font-size="40" font-weight="700" fill="#333a40">72<tspan font-size="24">%</tspan></text>
    <text x="110" y="142" text-anchor="middle" font-family="Open Sans, sans-serif" font-size="12" fill="#8a9299">Complete</text>
  </svg>
  <div class="pct-tag abs">72 %</div>
</section>

<section class="card section todo abs">
  <h2>Things left to do:</h2>
  <ul class="todo-list">
    <li>Tell us what type of designer you are<svg class="check" width="14" height="14"><rect x="1" y="1" width="12" height="12" fill="none" stroke="#1a8bc8"/><path d="M3.5 7l2.5 2.5 4.5-5" fill="none" stroke="#1a8bc8" stroke-width="1.6"/></svg></li>
    <li class="done">Verify your payment address<span class="complete">Complete</span></li>
    <li>Visit the Jobs Board<svg class="check" width="14" height="14"><rect x="1" y="1" width="12" height="12" fill="none" stroke="#1a8bc8"/><path d="M3.5 7l2.5 2.5 4.5-5" fill="none" stroke="#1a8bc8" stroke-width="1.6"/></svg></li>
    <li class="done">Add your profile pic<span class="complete">Complete</span></li>
    <li>Add an about me to your profile<svg class="check" width="14" height="14"><rect x="1" y="1" width="12" height="12" fill="none" stroke="#1a8bc8"/><path d="M3.5 7l2.5 2.5 4.5-5" fill="none" stroke="#1a8bc8" stroke-width="1.6"/></svg></li>
    <li>Review and accept the PixelHarbor quality standards<svg class="check" width="14" height="14"><rect x="1" y="1" width="12" height="12" fill="none" stroke="#1a8bc8"/><path d="M3.5 7l2.5 2.5 4.5-5" fill="none" stroke="#1a8bc8" stroke-width="1.6"/></svg></li>
    <li>Submit your first designs<svg class="check" width="14" height="14"><rect x="1" y="1" width="12" height="12" fill="none" stroke="#1a8bc8"/><path d="M3.5 7l2.5 2.5 4.5-5" fill="none" stroke="#1a8bc8" stroke-width="1.6"/></svg></li>
  </ul>
</section>

<section class="card section jobs abs">
  <h2>Recommended jobs</h2>
  <p class="intro">There is over <b>323815</b> waiting for you on these jobs that don't have any submissions yet.</p>
  <div class="job-grid">
    <div class="job"><span class="job-badge"></span><div><h4>Sealing Company Logo Design</h4><div class="job-meta"><span>3 days left</span><span>25</span><span>$ 200</span><span>Watchlist</span></div></div></div>
    <div class="job"><span class="job-badge"></span><div><h4>Sealing Company Logo Design</h4><div class="job-meta"><span>3 days left</span><span>25</span><span>$ 200</span><span>Watchlist</span></div></div></div>
    <div class="job"><span class="job-badge"></span><div><h4>Sealing Company Logo Design</h4><div class="job-meta"><span>3 days left</span><span>25</span><span>$ 200</span><span>Watchlist</span></div></div></div>
    <div class="job"><span class="job-badge"></span><div><h4>Sealing Company Logo Design</h4><div class="job-meta"><span>3 days left</span><span>25</span><span>$ 200</span><span>Watchlist</span></div></div></div>
    <div class="job"><span class="job-badge"></span><div><h4>Sealing Company Logo Design</h4><div class="job-meta"><span>3 days left</span><span>25</span><span>$ 200</span><span>Watchlist</span></div></div></div>
    <div class="job"><span class="job-badge"></span><div><h4>Sealing Company Logo Design</h4><div class="job-meta"><span>3 days left</span><span>25</span><span>$ 200</span><span>Watchlist</span></div></div></div>
  </div>
  <div class="pager"><span>Page 1</span><span>« Prev &nbsp; Next »</span></div>
</section>

<section class="card section achievements abs">
  <h2>Achievements</h2>
  <p class="intro">Earn PixelHarbor achievements as you unlock milestones.</p>
  <div class="ach-grid">
    <div class="ach"><span class="ach-icon"></span><div><b>True designer(Next)</b><small>Submit at least 1000 designs to contests</small></div></div>
    <div class="ach"><span class="ach-icon"></span><div><b>True designer(Next)</b><small>Submit at least 1000 designs to contests</small></div></div>
    <div class="ach"><span class="ach-icon"></span><div><b>Cha ching (Next)</b><small>Earn at least $25000 in winnings</small></div></div>
    <div class="ach"><span class="ach-icon"></span><div><b>Cha ching (Next)</b><small>Earn at least $25000 in winnings</small></div></div>
  </div>
</section>

<footer class="site-footer abs"></footer>
<div class="foot-col abs" style="left:60px"><h5>I need a...</h5><ul><li>Logo Design</li><li>Website Design</li><li>Business Card</li><li>Brochure Design</li><li>Banner Design</li><li>T-shirt Design</li><li>Packaging Design</li><li>Other Design</li></ul></div>
<div class="foot-col abs" style="left:200px"><h5>Find a...</h5><ul><li>Logo Designer</li><li>Web Designer</li><li>Graphic Designer</li><li>Illustrator</li><li>Print Designer</li><li>Freelancer</li></ul></div>
<div class="foot-col abs" style="left:340px"><h5>About us</h5><ul><li>How it works</li><li>Our Team</li><li>Careers</li><li>Press</li><li>Blog</li><li>Contact</li><li>Terms</li><li>Privacy</li></ul></div>
<div class="foot-col abs" style="left:500px"><h5>Popular pages</h5><div class="tags"><span>Logo Contest</span><span>Web Design</span><span>Business Cards</span><span>Flyers</span><span>Letterhead</span><span>Posters</span><span>Icons</span><span>Labels</span><span>Banners</span><span>Menus</span><span>Apps</span><span>Signage</span></div></div>
<div class="foot-col news abs" style="left:860px"><h5>✉ Subscribe to our newsletter</h5><input aria-label="Email address">
  <div class="socials"><span style="background:#3b5a98" role="img" aria-label="Social link"></span><span style="background:#39a9dc" role="img" aria-label="Social link"></span><span style="background:#d2452f" role="img" aria-label="Social link"></span><span style="background:#c8232c" role="img" aria-label="Social link"></span><span style="background:#d33" role="img" aria-label="Social link"></span><span style="background:#1f7bb6" role="img" aria-label="Social link"></span></div>
  <div class="flags"><span role="img" aria-label="Region"></span><span role="img" aria-label="Region"></span><span role="img" aria-label="Region"></span><span role="img" aria-label="Region"></span><span role="img" aria-label="Region"></span><span role="img" aria-label="Region"></span></div>
  <div class="foot-brand"><span class="brand-dot"></span>PixelHarbor</div>
</div>
<div class="copyright abs">Copyright © 2013 PixelHarbor Pty Ltd. All rights reserved. Terms of Use and Privacy Policy apply.</div>

</body>
</html>
```